Kelvara Constructions Business card and Logo

We are a building company that would like our current logo design copied with the "Kelvara Constructions" lines thicker.
We would also like our business cards copied with some minor copy changes. I have attached images of our logo and business cards.
We would like a standard size business card in landscape format rather than portrait.
On the back of the business card we would like a name added above the mobile number - "Teodor Marsk"
Can I please get high res file of the logo and business cards at completion of redesign?

```html
<!DOCTYPE html>
<html lang="en">
<head>
<meta charset="utf-8">
<title>Kelvara Constructions – Business Card</title>
<link rel="stylesheet" href="https://fonts.googleapis.com/css2?family=Open+Sans:wght@400;600;700&display=swap">
<style>
  :root {
    --bg: #e6e7e9;
    --card: #fafafa;
    --accent: #1ab0ea;
    --ink: #3a3a3a;
    --muted: #6f6f6f;
    --rule: #8a8a8a;
  }
  * { box-sizing: border-box; margin: 0; padding: 0; }
  html, body { width: 1200px; height: 911px; overflow: hidden; }
  body {
    background: var(--bg);
    font-family: "Open Sans", Arial, sans-serif;
    position: relative;
  }
  .card {
    position: absolute;
    width: 620px;
    height: 354px;
    background: var(--card);
    border-radius: 22px;
    box-shadow: 0 6px 18px rgba(0,0,0,0.12);
    overflow: hidden;
  }
  .card--back { left: 290px; top: 72px; }
  .card--front { left: 290px; top: 484px; }

  .accent-line {
    position: absolute;
    left: 0; right: 0;
    height: 4px;
    background: var(--accent);
  }
  .accent-square {
    position: absolute;
    width: 16px; height: 16px;
    background: var(--accent);
    transform: translate(-50%, -50%);
  }

  .brand-name {
    position: absolute;
    font-weight: 700;
    color: var(--accent);
    letter-spacing: 0.5px;
    line-height: 1.1;
  }
  .card--back .brand-name {
    left: 0; right: 0; top: 98px;
    text-align: center;
    font-size: 30px;
  }
  .card--back .accent-line { top: 178px; }
  .card--back .accent-square { left: 310px; top: 180px; }

  .card--front .brand-name {
    left: 42px; top: 62px;
    font-size: 26px;
  }
  .card--front .accent-line { top: 224px; }
  .card--front .accent-square { left: 250px; top: 226px; }

  .address {
    position: absolute;
    left: 42px; top: 270px;
    font-size: 17px;
    color: var(--ink);
  }

  .contact-block {
    position: absolute;
    left: 370px; top: 34px;
    width: 230px; height: 172px;
  }
  .contact-block__rule {
    position: absolute;
    left: 0; top: 0;
    width: 2px; height: 100%;
    background: var(--rule);
  }
  .person-name {
    position: absolute;
    left: 16px; top: 6px;
    font-size: 18px;
    font-weight: 600;
    color: var(--accent);
    text-transform: uppercase;
    letter-spacing: 0.5px;
  }
  .person-role {
    position: absolute;
    left: 16px; top: 32px;
    font-size: 15px;
    color: var(--muted);
  }
  .contact-list { list-style: none; position: absolute; left: 0; top: 74px; }
  .contact-list li {
    position: relative;
    padding-left: 18px;
    height: 24px;
    font-size: 13.5px;
    color: var(--ink);
    line-height: 24px;
  }
  .contact-list li::before {
    content: "";
    position: absolute;
    left: -5px; top: 7px;
    width: 11px; height: 11px;
    background: var(--accent);
  }
  .contact-list li.contact--web::before { display: none; }
</style>
</head>
<body>
  <section class="card card--back" aria-label="Business card back">
    <div class="brand-name">Kelvara Constructions</div>
    <div class="accent-line"></div>
    <div class="accent-square"></div>
  </section>

  <section class="card card--front" aria-label="Business card front">
    <div class="brand-name">Kelvara<br>Constructions</div>
    <div class="accent-line"></div>
    <div class="accent-square"></div>
    <p class="address">Harlow Yard, 118 Dunmore St. Calden</p>

    <div class="contact-block">
      <div class="contact-block__rule"></div>
      <h2 class="person-name">Teodor Marsk</h2>
      <p class="person-role">Managing Director</p>
      <ul class="contact-list">
        <li>012 555 0147</li>
        <li>012 555 0148</li>
        <li>info@kelvaraco.com</li>
        <li class="contact--web">kelvaraco.com</li>
      </ul>
    </div>
  </section>
</body>
</html>
```